" Temos como objetivo melhor atender as demandas atuais em TI com suporte de fácil acesso e analistas especializados com certificações que o mercado atual exige. Nossa equipe se dedica à prevenção, resolução de problemas e sugestões de melhorias do ambiente para garantir que seus servidores e aplicações estejam sempre no ar e funcionando, garantindo a continuidade dos negócios, foco das nossas soluções. "

```html
<!DOCTYPE html>
<html lang="pt-BR">
<head>
<meta charset="UTF-8">
<title>NUVTEC – Crachás de identificação</title>
<link rel="stylesheet" href="https://fonts.googleapis.com/css2?family=Montserrat:wght@300;400;500;600&display=swap">
<style>
  :root {
    --bg: #ff7a12;
    --navy: #15243d;
    --navy-soft: #1f3252;
    --white: #ffffff;
    --orange: #f26a1b;
    --yellow: #f7c21a;
    --text-dark: #2b2b2b;
    --text-muted: #555a63;
  }
  * { box-sizing: border-box; margin: 0; padding: 0; }
  html, body { width: 1200px; height: 1200px; overflow: hidden; }
  body {
    background: var(--bg);
    font-family: "Montserrat", Arial, sans-serif;
    display: flex;
    align-items: center;
    justify-content: center;
    gap: 80px;
  }
  .badge {
    position: relative;
    width: 420px;
    height: 640px;
    border-radius: 14px;
    overflow: hidden;
    background: var(--navy);
    box-shadow: 0 18px 40px rgba(0,0,0,0.25);
  }
  .brand {
    display: flex;
    align-items: center;
    justify-content: center;
    gap: 14px;
    color: var(--white);
    font-weight: 400;
    letter-spacing: 8px;
  }
  .brand-dot {
    width: 30px; height: 30px;
    border-radius: 50%;
    border: 3px solid var(--orange);
  }
  /* Front */
  .badge-front .brand { position: absolute; top: 70px; left: 0; right: 0; font-size: 34px; }
  .badge-front .swoosh { position: absolute; left: 0; bottom: 0; width: 420px; height: 640px; }
  .portrait {
    position: absolute;
    top: 150px; left: 105px;
    width: 210px; height: 290px;
    border: 5px solid var(--white);
    background: linear-gradient(160deg, #8f8f95 0%, #5b3b2e 45%, #c89a82 70%, #3a2a26 100%);
  }
  .holder-name {
    position: absolute;
    top: 520px; left: 0; right: 0;
    text-align: center;
    font-weight: 300;
    font-size: 34px;
    letter-spacing: 2px;
    color: var(--text-dark);
  }
  .holder-role {
    position: absolute;
    top: 566px; left: 0; right: 0;
    text-align: center;
    font-weight: 400;
    font-size: 16px;
    letter-spacing: 1px;
    color: var(--text-muted);
  }
  /* Back */
  .badge-back { padding: 140px 36px 0; }
  .field {
    height: 34px;
    background: var(--white);
    border-radius: 8px;
    margin-bottom: 14px;
    padding: 5px 12px;
    font-size: 10px;
    font-weight: 500;
    color: var(--text-muted);
  }
  .notice {
    margin-top: 86px;
    color: var(--white);
    font-size: 12.5px;
    line-height: 1.45;
    font-weight: 400;
  }
  .badge-back .brand { position: absolute; bottom: 70px; left: 0; right: 0; font-size: 40px; }
</style>
</head>
<body>
  <section class="badge badge-front">
    <svg class="swoosh" viewBox="0 0 420 640" aria-hidden="true">
      <path d="M0 400 C 120 330, 300 330, 420 380 L420 640 L0 640 Z" fill="#ffffff"/>
      <path d="M0 390 C 140 360, 260 400, 420 470 L420 500 C 260 430, 140 400, 0 430 Z" fill="var(--yellow)"/>
      <path d="M0 360 C 150 320, 280 340, 420 400 L420 425 C 280 370, 150 350, 0 395 Z" fill="var(--orange)"/>
    </svg>
    <div class="brand"><span class="brand-dot"></span>NUVTEC</div>
    <div class="portrait" role="img" aria-label="Foto do colaborador"></div>
    <p class="holder-name">LAURA MENEZES</p>
    <p class="holder-role">EXECUTIVA</p>
  </section>

  <section class="badge badge-back">
    <div class="field">NOME:</div>
    <div class="field">CPF:</div>
    <div class="field">FUNÇÃO:</div>
    <p class="notice">Esta identificação é de uso pessoal e intransferível.<br>
      O colaborador deverá usá-la obrigatoriamente em horário comercial.<br>
      Em caso de perda favor comunicar imediatamente ao Depto. Pessoal da empresa.</p>
    <div class="brand"><span class="brand-dot"></span>NUVTEC</div>
  </section>
</body>
</html>
```